Sleek, Professional Business Card Design Needed

Business Cards - Logo Attached.

We are a solar consulting company. We are national and want our cards to represent the professional high quality products that we offer.

Industry/Entity Type

Business

Contact Information for Business Card

n/a

Requirements
Must have
• Design
• Name
• Position
• Number
• Email
• Address
Should not have
• Not be too crowded

```html
<!DOCTYPE html>
<html lang="en">
<head>
<meta charset="utf-8">
<title>Brightline Solar – Business Card</title>
<link rel="stylesheet" href="https://fonts.googleapis.com/css2?family=Lato:wght@400;700&display=swap">
<style>
  :root {
    --bg: #e3e9ee;
    --card: #ffffff;
    --brand-blue: #1a8fd0;
    --brand-green: #8dc63f;
    --ink-dark: #3a3a3a;
    --ink-grey: #666a6e;
  }
  * { box-sizing: border-box; margin: 0; padding: 0; }
  html, body {
    width: 1200px; height: 800px; overflow: hidden;
    background: var(--bg);
    font-family: "Lato", sans-serif;
  }
  .canvas {
    position: relative; width: 1200px; height: 800px;
    display: flex; align-items: center; justify-content: center;
  }
  .card {
    position: relative; width: 1000px; height: 572px;
    background: var(--card);
    box-shadow: 0 10px 30px rgba(0,0,0,0.12);
    overflow: hidden;
  }
  .brand {
    position: absolute; left: 90px; top: 110px;
    display: flex; flex-direction: column; align-items: center; gap: 22px;
  }
  .brand-mark {
    width: 130px; height: 130px; border-radius: 50%;
    background: var(--brand-blue);
  }
  .brand-name {
    font-weight: 700; font-size: 38px; letter-spacing: 1px;
    color: var(--brand-blue); white-space: nowrap;
  }
  .person {
    position: absolute; right: 90px; top: 150px; text-align: right;
  }
  .person-name {
    font-weight: 700; font-size: 46px; color: var(--ink-dark); line-height: 1.05;
  }
  .person-title {
    font-weight: 700; font-size: 24px; color: var(--brand-green); margin-top: 2px;
  }
  .contact {
    position: absolute; right: 60px; top: 365px;
    font-size: 26px; color: var(--ink-grey); line-height: 34px;
    list-style: none;
  }
  .contact li { display: flex; justify-content: flex-end; align-items: center; gap: 16px; white-space: nowrap; }
  .contact .icon { width: 22px; height: 22px; flex: none; }
  .contact .spacer { width: 22px; flex: none; }
  .footer-band { position: absolute; left: 0; top: 0; width: 1000px; height: 572px; }
  .footer-url {
    position: absolute; left: 40px; bottom: 26px;
    font-size: 28px; color: #ffffff; letter-spacing: 0.5px;
  }
</style>
</head>
<body>
<div class="canvas">
  <section class="card">
    <svg class="footer-band" viewBox="0 0 1000 572" aria-hidden="true">
      <path d="M0 500 C 180 470, 420 445, 580 572 L0 572 Z" fill="var(--brand-blue)"/>
    </svg>
    <div class="footer-url">www.brightlinesolar.com</div>

    <div class="brand">
      <div class="brand-mark"></div>
      <div class="brand-name">BRIGHTLINE SOLAR</div>
    </div>

    <div class="person">
      <div class="person-name">Dana Mercer</div>
      <div class="person-title">Vice President</div>
    </div>

    <ul class="contact">
      <li><span>18750 Harbor Lane, Suite 4</span><span class="spacer"></span></li>
      <li><span>Riverton, Stateland 40817</span><span class="spacer"></span></li>
      <li><span>001 555 0199</span>
        <svg class="icon" viewBox="0 0 24 24" aria-hidden="true">
          <path d="M6.6 10.8a15 15 0 0 0 6.6 6.6l2.2-2.2a1 1 0 0 1 1-.25 11 11 0 0 0 3.6.6 1 1 0 0 1 1 1V20a1 1 0 0 1-1 1A17 17 0 0 1 3 4a1 1 0 0 1 1-1h3.5a1 1 0 0 1 1 1 11 11 0 0 0 .6 3.6 1 1 0 0 1-.25 1z" fill="var(--brand-green)"/>
        </svg>
      </li>
      <li><span>info@brightlinesolar.com</span>
        <svg class="icon" viewBox="0 0 24 24" aria-hidden="true">
          <rect x="2" y="5" width="20" height="14" fill="var(--brand-green)"/>
          <path d="M2 5 L12 13 L22 5" fill="none" stroke="#ffffff" stroke-width="1.6"/>
        </svg>
      </li>
    </ul>
  </section>
</div>
</body>
</html>
```